High Tech Real Estate Startup needs a business card

We are developing an innovative real estate marketing product based around advanced search and virtual reality.

We talk to people, we need business cards.

Target Market(s)

The target market is technology professionals and realtors.

Contact Information for Business Card

The information to be included will include

Name
Title
Phone Number
E-mail Address
www.quelzo.com

It should use simple iconography for each one of those fields.

Font styles to use
Other font styles liked:
• Co, Jubilat, Avenir

Colors

Designer to choose colors to be used in the design.

Requirements
Must have
• Clean aesthetic,
• Good use of negative space.
• It should use our company logo, shown in the attached file. It is able to use the negative of that logo (coloured font and white background) and I have attached other acceptable accent colours in a swatch file.
Should not have
• Should not be too busy
• No extraneous text (slogans, tag lines etc)

```html
<!DOCTYPE html>
<html lang="en">
<head>
<meta charset="utf-8">
<title>Quelzo Business Card</title>
<link href="https://fonts.googleapis.com/css2?family=Montserrat:wght@400;500;700&display=swap" rel="stylesheet">
<style>
  :root {
    --teal: #00b8bc;
    --white: #ffffff;
    --backdrop: #2a2a2a;
    --card-radius: 24px;
  }
  * { margin: 0; padding: 0; box-sizing: border-box; }
  html, body {
    width: 1200px; height: 880px; overflow: hidden;
    background: var(--backdrop);
    font-family: "Montserrat", sans-serif;
  }
  .canvas {
    position: relative; width: 1200px; height: 880px;
  }
  .card {
    position: absolute; left: 280px; width: 640px; height: 366px;
    border-radius: var(--card-radius); overflow: hidden;
  }
  .card-front {
    top: 60px; background: var(--teal);
    display: flex; align-items: center; justify-content: center;
  }
  .card-back { top: 456px; display: flex; }
  .wordmark {
    font-weight: 500; letter-spacing: 4px; line-height: 1;
  }
  .card-front .wordmark { color: var(--white); font-size: 84px; }
  .back-brand {
    width: 46%; background: var(--white);
    display: flex; align-items: center; justify-content: center;
  }
  .back-brand .wordmark { color: var(--teal); font-size: 60px; }
  .back-contact {
    width: 54%; background: var(--teal); color: var(--white);
    padding: 62px 30px 0 36px;
  }
  .person-name { font-weight: 700; font-size: 19px; letter-spacing: 0.5px; line-height: 1.1; }
  .person-title { font-weight: 400; font-size: 14px; margin-bottom: 30px; }
  .address { font-size: 15px; line-height: 1.35; margin-bottom: 6px; }
  .contact-list { list-style: none; font-size: 15px; line-height: 1.4; }
  .contact-list li { display: flex; align-items: center; gap: 8px; }
  .contact-list svg { width: 13px; height: 13px; flex: none; fill: var(--white); }
</style>
</head>
<body>
<main class="canvas">
  <section class="card card-front">
    <span class="wordmark">QUELZO</span>
  </section>

  <section class="card card-back">
    <div class="back-brand">
      <span class="wordmark">QUELZO</span>
    </div>
    <div class="back-contact">
      <p class="person-name">MARA ELLIOT</p>
      <p class="person-title">Manager</p>
      <p class="address">PO BOX 48 Harbour Lane<br>9th street Westbrook</p>
      <ul class="contact-list">
        <li>
          <svg viewBox="0 0 24 24" aria-hidden="true"><path d="M6.6 10.8a15.1 15.1 0 0 0 6.6 6.6l2.2-2.2a1 1 0 0 1 1-.25 11.4 11.4 0 0 0 3.6.57 1 1 0 0 1 1 1V20a1 1 0 0 1-1 1A17 17 0 0 1 3 4a1 1 0 0 1 1-1h3.5a1 1 0 0 1 1 1c0 1.25.2 2.45.57 3.6a1 1 0 0 1-.25 1z"/></svg>
          555-210-4471
        </li>
        <li>
          <svg viewBox="0 0 24 24" aria-hidden="true"><path d="M2 5h20v14H2zm2 2v.5l8 5 8-5V7zm0 2.9V17h16V9.9l-8 5z"/></svg>
          info@quelzomail.com
        </li>
        <li>
          <svg viewBox="0 0 24 24" aria-hidden="true"><path d="M12 2a10 10 0 1 0 0 20 10 10 0 0 0 0-20zm6.9 6h-2.9a15 15 0 0 0-1.4-3.6A8 8 0 0 1 18.9 8zM12 4c.8 1.2 1.5 2.5 1.9 4h-3.8c.4-1.5 1.1-2.8 1.9-4zM4.3 14a8 8 0 0 1 0-4h3.4a16 16 0 0 0 0 4zm.8 2h2.9a15 15 0 0 0 1.4 3.6A8 8 0 0 1 5.1 16zM8 8H5.1a8 8 0 0 1 4.3-3.6A15 15 0 0 0 8 8zm4 12c-.8-1.2-1.5-2.5-1.9-4h3.8c-.4 1.5-1.1 2.8-1.9 4zm2.3-6H9.7a14 14 0 0 1 0-4h4.6a14 14 0 0 1 0 4zm.3 5.6A15 15 0 0 0 16 16h2.9a8 8 0 0 1-4.3 3.6zM16.3 14a16 16 0 0 0 0-4h3.4a8 8 0 0 1 0 4z"/></svg>
          www.quelzo.com
        </li>
      </ul>
    </div>
  </section>
</main>
</body>
</html>
```